Jewelry store needs fully functional Ecommerce website

Web Design Brief for our E-commerce Jewelry retail store.
Description

We need a fully coded Shopify website. The Shopify site will need to be fully functional with an Ecommerce integration (fully integrated with Paylo and All other gateways) and will need to be SEO optimized.
We sell jewelry items like: rings, earrings, necklaces etc. The website should have an elegant, modern, professional, fun, look.

***We would like the website to look and function similarly to this website:
https://velvorisco.com

Color Preference
Colors to be used are white background with black font and light pink/ purple/ gold tints. We have attached our logo as reference.

Functionalities
The store will function like a typical Ecommerce jewelry store, using the products/categories as the starting page. Going into individual product pages by selecting images and leading to a detailed “buy now” page for the selected product.

Target Market
Jewelry lovers.

Should Not Have:
- - Dull and common design
- - Messy/unstructured navigation

Coded - Design and coding required
Target Audience are women from 16-50 years old.
We will need to be able to add products and make modifications to the website as needed.

We need the following apps installed and Operating:
-Tally Shift; Order Look Up (rename “track your order”) ; Help Center (Questions and Answers) ; Pemmo Reviews; TXT Nudge; Drenoza Email Marketing ; Plivet (Flockr messenger bump) ; Vantro multi- currency (translate currency to buyer) ; Discounted Upsell ; Easy Contact form App
We will need all products imported: (below is information for importing products). We will provide all links that serve entire active item product catalog in shopifys import format:
DataFeed:

If you are getting started with Shopify, a combination of the Shopify Import Format and XML feeds is ideal. The Shopify Import Format will output a file that can be uploaded into Shopify’s product database. After you import, you can use the XML feed and a third party app to keep the inventory up to date in real time, take down items that go out of stock etc., all without regular human intervention. There a several Shopify apps that can do this type of feed integration. We have had a good experience with Tally Shift, which is an app that can be configured to accept our XML feed and update products on a set schedule. You can even set your own margins based on our wholesale price with this app.

Shopify Formatted HTML TableTo make it easier to get started on Shopify, we included a format that outputs the required fields for a product import in Shopify. In order to use the embedded Excel file, first open the file (Auto-Shopify-Datasheet-Format.xslx), Refresh it (under Data tab), and then Save As with a new file name in a CSV (UTF-8) file. That file can then be split into smaller CSV files (if there is a limit on the number of products per file) for import into Shopify.

Target Market(s)

Jewelry Lovers

Industry/Entity Type

Jewelry Store

Coding

Number of Pages Required

5+ page

Colors
eda3c7
d3a5cc
ffffff

Requirements
Must have
• Color Preference
Colors to be used are white background with black font and light pink/ purple/ gold tints.

https://velvorisco.com
Should not have
• Should Not Have:

```html
<!DOCTYPE html>
<html lang="en">
<head>
<meta charset="utf-8">
<title>Product – Petite Rose Quartz Ring &amp; Twinkling Band</title>
<link href="https://fonts.googleapis.com/css2?family=Playfair+Display:wght@400;500&family=Poppins:wght@300;400;500;600&display=swap" rel="stylesheet">
<style>
:root{
  --ink:#222;
  --muted:#6b6b6b;
  --line:#e4e4e4;
  --pink:#eba6cb;
  --pink-text:#e58cb9;
  --lilac:#d3a5cc;
  --gold:#f5a623;
  --soft:#f3f3f5;
  --white:#fff;
}
*{margin:0;padding:0;box-sizing:border-box}
html,body{width:1200px;height:3873px;overflow:hidden;background:var(--white)}
body{position:relative;font-family:'Poppins',sans-serif;color:var(--ink)}
.abs{position:absolute}
.serif{font-family:'Playfair Display',serif;font-weight:400;text-transform:uppercase}
svg.star{width:1em;height:1em;fill:var(--gold);display:inline-block;vertical-align:middle}
svg.star.off{fill:#d6d6d6}

/* header */
.topbar{left:0;top:0;width:1200px;height:26px;background:#2b2b2b;color:#fff;font-size:11px;font-weight:600;letter-spacing:.5px;text-align:center;line-height:26px}
.nav{left:0;top:26px;width:1200px;height:69px}
.nav-links{left:88px;top:29px;display:flex;gap:28px;font-size:11px;font-weight:500;letter-spacing:.5px}
.logo{left:0;width:1200px;top:22px;text-align:center;font-family:'Playfair Display',serif;font-size:21px;font-weight:500;letter-spacing:.5px}
.nav-icons{left:912px;top:24px;display:flex;gap:32px}
.nav-icons svg{width:22px;height:22px;stroke:#444;fill:none;stroke-width:1.4}
.crumb{left:0;top:95px;width:1200px;height:51px;background:var(--soft);font-size:11px;font-weight:500;text-align:center;line-height:51px}

/* product */
.thumb{left:89px;width:101px;height:78px}
.main-photo{left:197px;top:214px;width:421px;height:428px;background:radial-gradient(ellipse 46% 42% at 52% 52%,#e2ad45 0,#d7a03a 55%,#f2e3da 80%,#f8f2f1 100%)}
.sale{left:218px;top:212px;width:42px;height:42px;background:#9a9a9a;color:#fff;font-size:10px;text-align:center;line-height:14px;padding-top:6px;clip-path:polygon(0 0,100% 0,100% 80%,50% 100%,0 80%)}
.info{left:683px;width:424px}
.stars-lg{top:210px;font-size:30px;display:flex;align-items:center;gap:2px}
.stars-lg span{font-size:20px;color:#999;margin-left:6px}
.p-title{top:256px;font-size:28px;line-height:31px}
.p-price{top:325px;font-size:22px;color:var(--pink-text);font-weight:500}
.material{top:365px;font-size:12px;font-weight:500;color:#444}
.material b{margin-left:12px;font-weight:500}
.rule{height:1px;background:var(--line)}
.opt-label{font-size:16px;font-weight:600}
.swatch{width:30px;height:30px;border-radius:50%}
.size{width:26px;height:26px;border-radius:50%;background:#f0f0f0;font-size:9px;font-weight:600;text-align:center;line-height:26px}
.size.on{background:#111;color:#fff}
.cart-btn{left:683px;top:522px;width:373px;height:51px;background:var(--pink);color:#fff;font-size:17px;font-weight:600;text-align:center;line-height:51px;letter-spacing:.5px}
.wish-btn{left:1060px;top:522px;width:50px;height:51px;background:var(--lilac);display:flex;align-items:center;justify-content:center}
.notes{left:683px;top:600px;font-size:12px;font-weight:500;line-height:22.5px;color:#333}
.acc{left:683px;width:424px;font-size:13px;font-weight:600;display:flex;justify-content:space-between;padding-bottom:10px;border-bottom:1px solid var(--line)}

/* styled with */
.styled-bg{left:0;top:874px;width:1200px;height:319px;background:var(--soft)}
.sec-title{left:0;width:1200px;text-align:center;font-size:40px}
.card{background:#fff;box-shadow:0 6px 24px rgba(0,0,0,.08)}
.s-card{top:1014px;width:266px;height:344px}
.s-card .ph{position:absolute;left:45px;top:22px;width:176px;height:150px}
.s-card .plus{position:absolute;right:14px;top:10px;font-size:24px;font-weight:300;color:#666}
.s-card h3{position:absolute;left:30px;top:198px;font-size:18px;line-height:23px}
.s-card .price{position:absolute;left:30px;top:254px;font-size:19px;color:#555;font-weight:300}
.s-card .view{position:absolute;right:45px;top:296px;font-size:13px;color:var(--pink-text);text-decoration:underline}
.arrow{font-size:26px;color:#555;font-weight:300}

/* reviews */
.badge{left:180px;top:1502px;width:83px;height:83px;border-radius:50%;background:var(--pink);color:#fff;font-family:'Playfair Display',serif;font-size:34px;text-align:center;line-height:83px}
.rev-summary{left:278px;top:1528px;font-size:27px;display:flex;align-items:center;gap:1px}
.rev-summary span{font-size:14px;color:#999;font-weight:600;margin-left:6px}
.write{left:787px;top:1522px;width:231px;height:47px;background:#f2f2f2;font-size:13px;font-weight:500;text-align:center;line-height:47px}
.rev-label{left:180px;top:1604px;font-size:13px;font-weight:600}
.rev{left:180px;width:840px;height:115px;border-bottom:1px solid var(--line)}
.rev .who{position:absolute;left:0;top:0;font-size:14px;font-weight:600}
.rev .who small{display:block;font-size:13px;font-weight:400;color:#444;margin-top:-2px}
.rev .who .st{font-size:17px;margin-top:2px;display:flex;gap:1px}
.rev .body{position:absolute;left:170px;top:-6px;width:555px}
.rev .body h4{font-size:16px;font-weight:500}
.rev .body p{font-size:13px;color:#777;line-height:21px;margin-top:6px}
.rev .date{position:absolute;right:0;top:24px;background:#f2f2f2;font-size:12px;padding:3px 8px}
.pager{left:0;width:1200px;top:2015px;display:flex;justify-content:center;align-items:center;gap:26px;font-size:17px}
.pager .on{width:46px;height:46px;border-radius:50%;background:#2b2b2b;color:#fff;text-align:center;line-height:46px}

/* gallery */
.gal{top:2211px;height:233px}
.gal-next{left:1140px;top:2307px;width:40px;height:40px;border-radius:50%;background:#fff;box-shadow:0 2px 8px rgba(0,0,0,.15);text-align:center;line-height:38px;font-size:20px}

/* also like */
.l-card{top:2602px;width:241px;height:361px;text-align:center}
.l-card .ph{position:absolute;left:35px;top:20px;width:171px;height:136px}
.l-card h3{position:absolute;left:0;width:100%;top:172px;font-size:16px;line-height:22px}
.l-card .price{position:absolute;left:0;width:100%;top:226px;font-size:20px;color:#555;font-weight:300}
.l-card .rate{position:absolute;left:0;width:100%;top:260px;font-size:15px;display:flex;justify-content:center;align-items:center;gap:1px}
.l-card .rate span{font-size:12px;color:#666;margin-left:8px}
.l-card .buy{position:absolute;left:30px;top:296px;width:181px;height:38px;background:var(--pink);color:#fff;font-size:14px;font-weight:600;line-height:38px}

/* features */
.feat{top:3050px;width:240px;text-align:center;font-size:14px;color:#555;line-height:21px}
.feat svg{width:62px;height:62px;stroke:var(--lilac);fill:none;stroke-width:1.6;margin-bottom:8px}

/* newsletter */
.news{left:0;top:3261px;width:1200px;height:221px;background:var(--lilac);background-image:radial-gradient(rgba(255,255,255,.12) 1px,transparent 1px);background-size:5px 5px}
.news h2{position:absolute;left:89px;top:50px;font-size:44px;line-height:45px;color:#fff}
.news p{position:absolute;left:89px;top:146px;font-size:15px;color:#fff;line-height:20px}
.news .field{position:absolute;left:632px;top:84px;width:476px;height:56px;background:#fff;border-radius:3px;display:flex;align-items:center;padding-left:20px;font-size:14px;color:#777;gap:10px}
.news .field b{position:absolute;right:6px;top:6px;width:120px;height:44px;background:var(--pink);color:#fff;font-size:13px;font-weight:600;text-align:center;line-height:44px}

/* footer */
.f-col{top:3558px}
.f-col h5{font-family:'Playfair Display',serif;font-weight:400;font-size:18px;text-transform:uppercase;margin-bottom:16px}
.f-col li{list-style:none;font-size:13px;color:#444;line-height:27px}
.contact-item{display:flex;gap:10px;font-size:13px;color:#444;line-height:18px;margin-bottom:10px}
.contact-item svg{width:14px;height:14px;fill:var(--lilac);flex:none;margin-top:2px}
.social{display:flex;gap:8px;margin-bottom:34px}
.social span{display:flex;align-items:center;gap:4px;font-size:11px;color:#444}
.social i{width:14px;height:14px;border-radius:50%;background:var(--lilac);display:inline-block}
.pay{display:flex;gap:8px}
.pay span{width:50px;height:30px;border:1px solid var(--line);border-radius:3px;font-size:10px;font-weight:500;text-align:center;line-height:28px;color:#444}
.f-rule{left:89px;top:3820px;width:1022px;height:1px;background:var(--line)}
.copy{left:0;width:1200px;top:3838px;text-align:center;font-size:13px;font-weight:500}
.totop{left:1132px;top:3799px;width:42px;height:42px;border-radius:50%;background:var(--pink);color:#fff;text-align:center;line-height:42px;font-size:16px}
</style>
</head>
<body>
<svg width="0" height="0" style="position:absolute">
  <defs>
    <symbol id="star" viewBox="0 0 24 24"><path d="M12 1.8l3.1 6.5 7.1.9-5.2 4.9 1.3 7.1L12 17.8l-6.3 3.4 1.3-7.1L1.8 9.2l7.1-.9z"/></symbol>
  </defs>
</svg>

<header>
  <div class="abs topbar">FREE US SHIPPING ON ORDERS $50+</div>
  <div class="abs nav">
    <nav class="abs nav-links"><span>HOME</span><span>SHOP</span><span>PRODUCT</span></nav>
    <div class="abs logo">LOGO HERE</div>
    <div class="abs nav-icons">
      <svg viewBox="0 0 24 24"><circle cx="11" cy="11" r="7"/><path d="M16 16l5 5"/></svg>
      <svg viewBox="0 0 24 24"><circle cx="12" cy="8" r="4"/><path d="M4 21c1-5 15-5 16 0"/></svg>
      <svg viewBox="0 0 24 24"><path d="M12 20s-8-5-8-11a4.5 4.5 0 0 1 8-2.5A4.5 4.5 0 0 1 20 9c0 6-8 11-8 11z"/></svg>
      <svg viewBox="0 0 24 24"><path d="M5 8h14l-1 13H6z"/><path d="M9 8V6a3 3 0 0 1 6 0v2"/><circle cx="19" cy="20" r="2.5" fill="#eba6cb" stroke="none"/></svg>
    </div>
  </div>
  <div class="abs crumb">HOME / PETITE ROSE QUARTZ RING &amp; TWINKLING BAND</div>
</header>

<main>
  <section class="product">
    <div class="abs thumb" style="top:214px;background:radial-gradient(circle at 50% 50%,#dda08d 0,#e9c3b6 35%,#f7f1f0 70%)" role="img" aria-label="Rose gold ring thumbnail"></div>
    <div class="abs thumb" style="top:302px;background:radial-gradient(circle at 50% 50%,#b58a63 0,#d9c2ad 35%,#f6f4f2 70%)" role="img" aria-label="Two-tone ring pair thumbnail"></div>
    <div class="abs thumb" style="top:389px;background:radial-gradient(circle at 50% 50%,#d9a73c 0,#ecd29c 35%,#f8f5ee 70%)" role="img" aria-label="Gold wrap ring thumbnail"></div>
    <div class="abs thumb" style="top:477px;background:radial-gradient(circle at 50% 50%,#9a9a9a 0,#d3d3d3 35%,#f7f7f7 70%)" role="img" aria-label="Silver ring thumbnail"></div>
    <div class="abs main-photo" role="img" aria-label="Gold coiled nail ring with pavé stones"></div>
    <div class="abs sale">50%<br>OFF</div>

    <div class="abs info stars-lg">
      <svg class="star"><use href="#star"/></svg><svg class="star"><use href="#star"/></svg><svg class="star"><use href="#star"/></svg><svg class="star"><use href="#star"/></svg><svg class="star"><use href="#star"/></svg><span>(473)</span>
    </div>
    <h1 class="abs info serif p-title">Some Product Heading<br>Goes Here</h1>
    <div class="abs info p-price">$99.00</div>
    <div class="abs info material">MATERIAL:<b>14KT YELLOW GOLD VERMEIL</b></div>
    <div class="abs info rule" style="top:402px"></div>

    <div class="abs opt-label" style="left:683px;top:427px">COLOURS</div>
    <div class="abs" style="left:685px;top:460px;display:flex;gap:8px">
      <div class="swatch" style="background:#d99a8a"></div>
      <div class="swatch" style="background:#c9a45a;display:flex;align-items:center;justify-content:center"><svg width="12" height="12" viewBox="0 0 12 12"><path d="M2 6l3 3 5-6" stroke="#fff" stroke-width="1.8" fill="none"/></svg></div>
      <div class="swatch" style="background:#b8b8b8"></div>
    </div>
    <div class="abs opt-label" style="left:825px;top:427px">SIZE</div>
    <div class="abs" style="left:829px;top:462px;display:flex;gap:10px">
      <div class="size">S</div><div class="size">M</div><div class="size on">L</div><div class="size">XL</div><div class="size">XXL</div><div class="size">3XL</div>
    </div>

    <div class="abs cart-btn">ADD TO CART</div>
    <div class="abs wish-btn"><svg width="20" height="18" viewBox="0 0 24 22"><path d="M12 21s-10-6-10-13A5.5 5.5 0 0 1 12 5a5.5 5.5 0 0 1 10 3c0 7-10 13-10 13z" fill="#fff"/></svg></div>

    <div class="abs notes">DROP A HINT? CLICK HERE<br>FREE US SHIPPING ON ORDERS OVER $50<br>HASSLE FREE 30 DAY RETURNS</div>

    <div class="abs acc" style="top:698px"><span>DESCRIPTION</span><span>›</span></div>
    <div class="abs acc" style="top:740px"><span>JEWELLRY</span><span>›</span></div>
    <div class="abs acc" style="top:783px"><span>SHIPPING &amp; RETURNS</span><span>›</span></div>
  </section>

  <section class="styled-with">
    <div class="abs styled-bg"></div>
    <h2 class="abs serif sec-title" style="top:948px">Most Often Styled With</h2>
    <div class="abs arrow" style="left:128px;top:1086px">‹</div>
    <div class="abs arrow" style="left:1058px;top:1086px">›</div>

    <article class="abs card s-card" style="left:183px">
      <div class="ph" style="background:radial-gradient(ellipse 45% 50% at 50% 50%,#8e8e8e 0,#c8c8c8 45%,#fff 80%)" role="img" aria-label="Silver chandelier earrings"></div>
      <span class="plus">+</span>
      <h3 class="serif">Some Our Product<br>Heading Goes</h3>
      <div class="price">$99.00</div>
      <a class="view">VIEW ITEM</a>
    </article>
    <article class="abs card s-card" style="left:468px">
      <div class="ph" style="background:radial-gradient(ellipse 48% 42% at 50% 50%,#a9a9a9 0,#dcdcdc 45%,#fff 80%)" role="img" aria-label="Diamond solitaire ring"></div>
      <span class="plus">+</span>
      <h3 class="serif">Some Our Product<br>Heading Goes</h3>
      <div class="price">$99.00</div>
      <a class="view">VIEW ITEM</a>
    </article>
    <article class="abs card s-card" style="left:752px">
      <div class="ph" style="background:radial-gradient(ellipse 50% 42% at 50% 50%,#707070 0,#bdbdbd 45%,#fff 80%)" role="img" aria-label="Silver chain ID bracelet"></div>
      <span class="plus">+</span>
      <h3 class="serif">Some Our Product<br>Heading Goes</h3>
      <div class="price">$99.00</div>
      <a class="view">VIEW ITEM</a>
    </article>
  </section>

  <section class="reviews">
    <h2 class="abs serif sec-title" style="top:1440px">Customer Reviews</h2>
    <div class="abs badge">5.0</div>
    <div class="abs rev-summary">
      <svg class="star"><use href="#star"/></svg><svg class="star"><use href="#star"/></svg><svg class="star"><use href="#star"/></svg><svg class="star"><use href="#star"/></svg><svg class="star"><use href="#star"/></svg><span>(473) REVIEWS</span>
    </div>
    <div class="abs write">WRITE A REVIEW</div>
    <div class="abs rev-label">REVIEWS</div>
    <svg class="abs" style="left:996px;top:1602px" width="22" height="20" viewBox="0 0 22 20" fill="none" stroke="#444" stroke-width="1.3"><path d="M1 4h20M1 10h20M1 16h20"/><circle cx="14" cy="4" r="2.2" fill="#fff"/><circle cx="7" cy="10" r="2.2" fill="#fff"/><circle cx="14" cy="16" r="2.2" fill="#fff"/></svg>
    <div class="abs rule" style="left:180px;top:1630px;width:840px"></div>

    <div class="abs rev" style="top:1663px">
      <div class="who">ARIELLE C.<small>Verified Buyer</small><div class="st"><svg class="star"><use href="#star"/></svg><svg class="star"><use href="#star"/></svg><svg class="star"><use href="#star"/></svg><svg class="star"><use href="#star"/></svg><svg class="star"><use href="#star"/></svg></div></div>
      <div class="body"><h4>Beautiful!! Love it so much!</h4><p>Bibendum auctor, nisi elit consequat ipsum, nec sagittis sem nibh id elit. Duis<br>sed odio sit amet nibh vulputate cursus a sit...</p></div>
      <span class="date">31/01/21</span>
    </div>
    <div class="abs rev" style="top:1778px">
      <div class="who">ARIELLE C.<small>Verified Buyer</small><div class="st"><svg class="star"><use href="#star"/></svg><svg class="star"><use href="#star"/></svg><svg class="star"><use href="#star"/></svg><svg class="star"><use href="#star"/></svg><svg class="star"><use href="#star"/></svg></div></div>
      <div class="body"><h4>Beautiful!! Love it so much!</h4><p>Bibendum auctor, nisi elit consequat ipsum, nec sagittis sem nibh id elit. Duis<br>sed odio sit amet nibh vulputate cursus a sit...</p></div>
      <span class="date">31/01/21</span>
    </div>
    <div class="abs rev" style="top:1893px">
      <div class="who">ARIELLE C.<small>Verified Buyer</small><div class="st"><svg class="star"><use href="#star"/></svg><svg class="star"><use href="#star"/></svg><svg class="star"><use href="#star"/></svg><svg class="star"><use href="#star"/></svg><svg class="star"><use href="#star"/></svg></div></div>
      <div class="body"><h4>Beautiful!! Love it so much!</h4><p>Bibendum auctor, nisi elit consequat ipsum, nec sagittis sem nibh id elit. Duis<br>sed odio sit amet nibh vulputate cursus a sit...</p></div>
      <span class="date">31/01/21</span>
    </div>

    <nav class="abs pager"><span>‹</span><span>1</span><span class="on">2</span><span>3</span><span>...</span><span>15</span><span>›</span></nav>
  </section>

  <section class="gallery">
    <h2 class="abs serif" style="left:89px;top:2143px;font-size:40px">Follow Us On Pictora</h2>
    <div class="abs gal" style="left:89px;width:200px;background:linear-gradient(135deg,#cfe3ea,#a9d0e0)" role="img" aria-label="Blue ribbon with diamonds"></div>
    <div class="abs gal" style="left:295px;width:200px;background:linear-gradient(135deg,#9fd8c4,#e29a6b)" role="img" aria-label="Colourful beaded bracelets"></div>
    <div class="abs gal" style="left:499px;width:200px;background:linear-gradient(135deg,#f6c3b6,#c0243a)" role="img" aria-label="Pearl necklace around red ring box"></div>
    <div class="abs gal" style="left:705px;width:200px;background:linear-gradient(135deg,#e9d6c6,#e6a3c1)" role="img" aria-label="Gold zigzag cuff on pink"></div>
    <div class="abs gal" style="left:910px;width:200px;background:linear-gradient(135deg,#7fb3c9,#8a6a55)" role="img" aria-label="Hands wearing rings"></div>
    <div class="abs gal" style="left:1113px;width:87px;background:linear-gradient(135deg,#f4f1ee,#dcd4cc)" role="img" aria-label="Delicate rings on white"></div>
    <div class="abs gal-next">›</div>
  </section>

  <section class="also-like">
    <h2 class="abs serif sec-title" style="top:2520px">You May Also Like</h2>
    <article class="abs card l-card" style="left:89px">
      <div class="ph" style="background:radial-gradient(ellipse 48% 42% at 50% 50%,#a9a9a9 0,#dcdcdc 45%,#fff 80%)" role="img" aria-label="Diamond solitaire ring"></div>
      <h3 class="serif">Some Our Product<br>Heading Goes</h3><div class="price">$99.00</div>
      <div class="rate"><svg class="star"><use href="#star"/></svg><svg class="star"><use href="#star"/></svg><svg class="star"><use href="#star"/></svg><svg class="star"><use href="#star"/></svg><svg class="star off"><use href="#star"/></svg><span>25 reviews</span></div>
      <div class="buy">BUY NOW</div>
    </article>
    <article class="abs card l-card" style="left:347px">
      <div class="ph" style="background:radial-gradient(ellipse 40% 48% at 50% 50%,#cf8f70 0,#ebcbb9 45%,#fff 80%)" role="img" aria-label="Rose gold engagement ring"></div>
      <h3 class="serif">Some Our Product<br>Heading Goes</h3><div class="price">$99.00</div>
      <div class="rate"><svg class="star"><use href="#star"/></svg><svg class="star"><use href="#star"/></svg><svg class="star"><use href="#star"/></svg><svg class="star"><use href="#star"/></svg><svg class="star off"><use href="#star"/></svg><span>25 reviews</span></div>
      <div class="buy">BUY NOW</div>
    </article>
    <article class="abs card l-card" style="left:608px">
      <div class="ph" style="background:radial-gradient(ellipse 48% 42% at 50% 50%,#8d8572 0,#d4cfc2 45%,#fff 80%)" role="img" aria-label="Stacked wedding bands"></div>
      <h3 class="serif">Some Our Product<br>Heading Goes</h3><div class="price">$99.00</div>
      <div class="rate"><svg class="star"><use href="#star"/></svg><svg class="star"><use href="#star"/></svg><svg class="star"><use href="#star"/></svg><svg class="star"><use href="#star"/></svg><svg class="star off"><use href="#star"/></svg><span>25 reviews</span></div>
      <div class="buy">BUY NOW</div>
    </article>
    <article class="abs card l-card" style="left:868px">
      <div class="ph" style="background:radial-gradient(ellipse 48% 40% at 50% 50%,#d39a72 0,#efd3bf 45%,#fff 80%)" role="img" aria-label="Rose gold open bangle"></div>
      <h3 class="serif">Some Our Product<br>Heading Goes</h3><div class="price">$99.00</div>
      <div class="rate"><svg class="star"><use href="#star"/></svg><svg class="star"><use href="#star"/></svg><svg class="star"><use href="#star"/></svg><svg class="star"><use href="#star"/></svg><svg class="star off"><use href="#star"/></svg><span>25 reviews</span></div>
      <div class="buy">BUY NOW</div>
    </article>
  </section>

  <section class="features">
    <div class="abs feat" style="left:128px">
      <svg viewBox="0 0 64 64"><path d="M6 20h34v22H6zM40 28h10l8 8v6H40z"/><circle cx="16" cy="46" r="4"/><circle cx="48" cy="46" r="4"/><path d="M2 26h10M2 32h8"/></svg>
      <div>Free US Shipping On<br>Orders Over $50</div>
    </div>
    <div class="abs feat" style="left:360px">
      <svg viewBox="0 0 64 64"><path d="M16 26l16-8 16 8v20l-16 8-16-8z"/><path d="M16 26l16 8 16-8M32 34v20"/><path d="M22 12a14 14 0 0 1 22 4l2-6"/></svg>
      <div>Hassle-Free Returns Easily<br>Exchange Or Return Items</div>
    </div>
    <div class="abs feat" style="left:606px">
      <svg viewBox="0 0 64 64"><path d="M18 30h8V14c0-4 6-4 6 0v8h10c3 0 4 3 3 5l-4 10H26"/><path d="M14 50l2-4 2 4 4 1-3 3 1 4-4-2-4 2 1-4-3-3zM32 50l2-4 2 4 4 1-3 3 1 4-4-2-4 2 1-4-3-3zM50 50l2-4 2 4 4 1-3 3 1 4-4-2-4 2 1-4-3-3z"/></svg>
      <div>Over 1 Million Followers<br>&amp; 11,000 5-Star Reviews</div>
    </div>
    <div class="abs feat" style="left:828px">
      <svg viewBox="0 0 64 64"><path d="M18 8c0 16 8 22 14 22s14-6 14-22"/><path d="M22 8c0 12 5 18 10 18s10-6 10-18"/><path d="M24 34l8-6 8 6-8 14z"/><path d="M24 34h16"/></svg>
      <div>Authentic women<br>Jewlry</div>
    </div>
  </section>

  <section class="abs news">
    <h2 class="serif">Subscribe<br>Newsletter</h2>
    <p>By subscribing to our mailing list you will always be updated<br>with the latest news from us.</p>
    <div class="field">
      <svg width="16" height="12" viewBox="0 0 16 12"><rect x="0" y="0" width="16" height="12" rx="1" fill="#888"/><path d="M1 1l7 6 7-6" stroke="#fff" fill="none"/></svg>
      Enter your email address<b>SIGN ME UP!</b>
    </div>
  </section>
</main>

<footer>
  <div class="abs f-col" style="left:128px">
    <h5>Let Us Help You</h5>
    <ul><li>Search</li><li>About Us</li><li>Ring Size Guide</li><li>Jewelry Care Guide</li><li>Shipping</li><li>Contact</li><li>FAQ'S</li></ul>
  </div>
  <div class="abs f-col" style="left:364px">
    <h5>Information</h5>
    <ul><li>Site Map</li><li>Terms &amp; Condition</li><li>Privacy Policy</li><li>FAQ's</li><li>Customer Service</li><li>Disclaimer</li></ul>
  </div>
  <div class="abs f-col" style="left:588px;width:230px">
    <h5>Contact Us</h5>
    <div class="contact-item"><svg viewBox="0 0 16 16"><path d="M1 3h14v10H1z"/></svg><span>Email:<br>care@lumeria-shop.com</span></div>
    <div class="contact-item"><svg viewBox="0 0 16 16"><path d="M4 1l3 3-2 2c1 2 3 4 5 5l2-2 3 3-2 3C7 15 1 9 1 3z"/></svg><span>Phone:<br>(+61) 400 555 019</span></div>
    <div class="contact-item"><svg viewBox="0 0 16 16"><path d="M8 1a5 5 0 0 1 5 5c0 4-5 9-5 9S3 10 3 6a5 5 0 0 1 5-5z"/></svg><span>Office Location:<br>Some address line goes here<br>city name</span></div>
  </div>
  <div class="abs f-col" style="left:850px">
    <h5>Stay Connected</h5>
    <div class="social"><span><i></i>Flockr</span><span><i></i>Twyne</span><span><i></i>Pictora</span></div>
    <h5>Payment Method</h5>
    <div class="pay"><span>Paylo</span><span>Verra</span><span>Mondo</span><span>Distra</span></div>
  </div>
  <div class="abs f-rule"></div>
  <div class="abs copy">© COPYRIGHT 2021 - ALL RIGHTS RESERVED</div>
  <div class="abs totop">↑</div>
</footer>
</body>
</html>
```